Wound Care Flyer

Looking for a Trifold brochure that is modern and has a high aesthetic. (Specialty services) Would like the colors to center around Black and Gold. Possibly updating the logo. Attached is the old brochure and a document about our services.

```html
<!DOCTYPE html>
<html lang="en">
<head>
<meta charset="utf-8">
<title>Cedar Ridge Wounds – Trifold Brochure</title>
<link href="https://fonts.googleapis.com/css2?family=Poppins:wght@400;500;600;700&display=swap" rel="stylesheet">
<style>
:root{
  --black:#161514;
  --gold:#b8935a;
  --gold-light:#d7b77c;
  --white:#ffffff;
  --paper:#f7f7f6;
  --stage:#e3e3e3;
  --ink:#1d1d1d;
}
*{margin:0;padding:0;box-sizing:border-box}
html,body{width:1200px;height:3315px;overflow:hidden}
body{background:var(--stage);font-family:'Poppins',sans-serif;color:var(--ink);position:relative}
.spread{position:absolute;left:30px;width:1140px;height:880px;background:var(--white);overflow:hidden;box-shadow:0 10px 24px rgba(0,0,0,.25)}
.spread--outside{top:690px}
.spread--inside{top:1710px}
.abs{position:absolute}
.shapes{position:absolute;left:0;top:0}
.photo{position:absolute}
.photo--cool{background:linear-gradient(135deg,#cfd8df,#8ea3b4 55%,#5e6f7d)}
.photo--warm{background:linear-gradient(160deg,#f1ece6,#c7b3a3 55%,#7d8fa6)}
.photo--teal{background:linear-gradient(150deg,#2f8fa2,#4fb6c6 45%,#1c5c6c)}
.photo--clinic{background:linear-gradient(150deg,#eef1f3,#b9c7cf 50%,#a43b36 85%)}
.photo--portrait{background:linear-gradient(160deg,#efebe7,#d8cfc8)}
.framed{border:3px solid var(--black)}
.brand{position:absolute;text-align:center;width:200px}
.brand__ring{width:50px;height:50px;border:2px solid var(--gold);border-radius:50%;margin:0 auto 8px}
.brand__name{color:var(--gold);font-size:11px;font-weight:500;letter-spacing:3px;line-height:1.35}
.tag{position:absolute;background:linear-gradient(90deg,var(--gold),var(--gold-light));clip-path:polygon(8% 0,100% 0,92% 100%,0 100%);color:var(--black);font-weight:600;display:flex;align-items:center;justify-content:center}
.body-text{font-size:10.8px;line-height:1.38;font-weight:500}
.gold{color:var(--gold)}
.white{color:var(--white)}
.h-gold{color:var(--gold);font-weight:600;line-height:1.1}
.areas{font-size:10.5px;font-weight:600;line-height:1.7}
.areas i{color:var(--gold);font-style:normal;margin:0 2px 0 6px}
.areas i:first-child{margin-left:0}
.contact{position:absolute;left:380px;width:380px;text-align:center;color:var(--white)}
.contact__title{font-size:21px;font-weight:500;letter-spacing:.5px}
.contact__dot{width:7px;height:7px;border-radius:50%;background:var(--gold);margin:0 auto 4px}
.contact__line{font-size:13px;font-weight:500}
.headline{position:absolute;left:760px;width:380px;text-align:center}
.headline__main{font-size:38px;font-weight:600;line-height:1;color:var(--white)}
.headline__gold{font-size:38px;font-weight:600;line-height:1.05;color:var(--gold)}
.headline__sub{font-size:11px;font-weight:700;color:var(--white);line-height:1.3;margin-top:14px}
.service-box{width:196px;margin:7px auto 0;border:1px solid var(--white);color:var(--white);font-size:9.5px;padding:1px 0}
.web{font-size:13px;color:var(--white)}
.web b{color:var(--gold);font-weight:600}
.treat-list{display:grid;grid-template-columns:1fr 1fr;gap:3px 16px;font-size:9.5px;line-height:1.25;list-style:none}
.treat-list li::before{content:"▸ ";color:var(--gold)}
.partner{position:absolute;left:785px;width:340px;display:flex;gap:12px}
.partner__icon{flex:0 0 30px;height:30px;border:1.5px solid var(--white);border-radius:50%;display:flex;align-items:center;justify-content:center}
.partner__title{color:var(--gold);font-size:12.5px;font-weight:600;line-height:1.2}
.partner__text{color:var(--white);font-size:10px;line-height:1.3}
.focus i{color:var(--gold);font-style:normal}
</style>
</head>
<body>

<section class="spread spread--outside">
  <svg class="shapes" width="1140" height="880" viewBox="0 0 1140 880">
    <polygon points="0,880 0,852 380,640 380,672 40,880" fill="var(--gold)"/>
    <polygon points="40,880 380,672 760,462 760,0 1140,0 1140,880" fill="var(--black)"/>
  </svg>

  <!-- Left panel -->
  <div class="tag" style="left:40px;top:55px;width:160px;height:30px;font-size:18px">ABOUT US</div>
  <p class="abs body-text" style="left:40px;top:100px;width:300px">We provide an additional layer of expertise by utilizing advanced the advanced technology of biological skin substitute grafts. We pride ourselves in working in close coordination with the patient's care team, including home health services and the primary care physician (PCP). We ensure seamless integration without duplicating services prioritizing collaborative care, sharing detailed notes and working closely with the patient's home health team on days between visits.</p>
  <p class="abs gold" style="left:40px;top:278px;font-size:11px;font-weight:600">SERVING THE GREATER NORTH HOUSTON</p>
  <div class="abs areas" style="left:40px;top:296px">
    <div><i>▸</i>Spring <i>▸</i>The Woodlands <i>▸</i>Tomball</div>
    <div><i>▸</i>Conroe <i>▸</i>Willis <i>▸</i>Magnolia</div>
    <div><i>▸</i>Montgomery <i>▸</i>Cypress</div>
  </div>
  <div class="photo photo--cool" role="img" aria-label="Clinician reviewing an X-ray with a patient" style="left:40px;top:370px;width:292px;height:218px"></div>
  <div class="photo photo--warm" role="img" aria-label="Clinician examining a seated patient's leg" style="left:40px;top:604px;width:292px;height:218px"></div>

  <!-- Middle panel -->
  <div class="brand" style="left:470px;top:28px">
    <div class="brand__ring"></div>
    <div class="brand__name">CEDAR RIDGE<br>WOUNDS</div>
  </div>
  <svg class="shapes" width="1140" height="880" viewBox="0 0 1140 880">
    <circle cx="570" cy="340" r="132" fill="none" stroke="var(--gold)" stroke-width="2"/>
  </svg>
  <div class="photo photo--portrait" role="img" aria-label="Portrait photo of the nurse practitioner" style="left:480px;top:222px;width:180px;height:380px"></div>
  <div class="tag" style="left:405px;top:590px;width:270px;height:32px;font-size:18px;font-weight:500">Dana Whitfield, FNP-C</div>
  <div class="contact" style="top:648px">
    <div class="contact__title">CONTACT US</div>
    <div style="margin-top:18px"><div class="contact__dot"></div><div class="contact__line">O: (555) 014-2871</div></div>
    <div style="margin-top:14px"><div class="contact__dot"></div><div class="contact__line">F: (555) 014-3390</div></div>
    <div style="margin-top:14px"><div class="contact__dot"></div><div class="contact__line">cedarridgewounds@mail.com</div></div>
    <div style="margin-top:14px"><div class="contact__dot"></div><div class="contact__line">www.cedarridgewounds.com</div></div>
  </div>

  <!-- Right panel -->
  <div class="brand" style="left:850px;top:28px">
    <div class="brand__ring"></div>
    <div class="brand__name">CEDAR RIDGE<br>WOUNDS</div>
  </div>
  <svg class="shapes" width="1140" height="880" viewBox="0 0 1140 880">
    <polyline points="760,448 950,522 1140,448" fill="none" stroke="var(--white)" stroke-width="10"/>
    <polyline points="760,462 950,536 1140,462" fill="none" stroke="var(--gold)" stroke-width="6"/>
  </svg>
  <div class="photo photo--cool" role="img" aria-label="Doctor dressing a patient's leg wound in a clinic" style="left:760px;top:148px;width:380px;height:360px;clip-path:polygon(0 0,100% 0,100% 78%,50% 100%,0 78%)"></div>
  <div class="headline" style="top:568px">
    <div class="headline__main">ADVANCED</div>
    <div class="headline__gold">WOUND CARE</div>
    <div class="headline__sub">SPECIALIZING IN BIOLOGIC SKIN<br>SUBSTITUTES TO TREAT</div>
    <div class="service-box" style="margin-top:12px">Pressure Injuries</div>
    <div class="service-box">Diagnostic Testing</div>
    <div class="service-box">Debridements</div>
    <div class="service-box">Multidisciplinary Collaboration</div>
    <div class="web" style="margin-top:12px">www.<b>cedarridgewounds</b>.com</div>
  </div>
</section>

<section class="spread spread--inside">
  <svg class="shapes" width="1140" height="880" viewBox="0 0 1140 880">
    <polygon points="0,340 190,398 380,340 380,880 0,880" fill="var(--black)"/>
    <polyline points="0,322 190,380 380,322" fill="none" stroke="var(--gold)" stroke-width="7"/>
    <polygon points="45,0 335,0 335,318 190,366 45,318" fill="var(--black)"/>
    <polygon points="760,455 1140,338 1140,880 760,880" fill="var(--black)"/>
    <polygon points="760,440 1140,322 1140,336 760,454" fill="var(--gold)"/>
  </svg>

  <!-- Left panel -->
  <div class="photo photo--teal" role="img" aria-label="Surgeon in scrubs treating a patient's arm" style="left:55px;top:0;width:270px;height:352px;clip-path:polygon(0 0,100% 0,100% 87%,50% 100%,0 87%)"></div>
  <div class="abs" style="left:40px;top:438px;width:310px">
    <div class="white" style="font-size:22px;font-weight:600;line-height:1.1">CEDAR RIDGE WOUNDS:</div>
    <div class="h-gold" style="font-size:19px;margin-top:6px">MOBILE WOUND CARE</div>
    <p class="white focus" style="font-size:10px;margin-top:6px;line-height:1.35">With a focus on <i>▸</i> <b>convenience</b> <i>▸</i><b>expertise</b><br><i>▸</i> <b>compassion</b></p>
    <p class="white" style="font-size:10.2px;line-height:1.35;margin-top:12px">we bring the highest standard of wound care directly to the patient's home. Working side-by-side with the patient's physician, our team of experienced specialists utilize cutting-edge technology and personalized treatment plans to ensure optimal healing and comfort. From thorough wound assessments to advanced therapies and ongoing support, we prioritize the well-being of our patients every step of the way.</p>
    <p class="white" style="font-size:10.2px;line-height:1.35;margin-top:12px">Whether it's managing chronic wounds, post-surgery recovery, we go above and beyond to provide comprehensive and compassionate care. With our concierge approach, we aim to make the healing journey as seamless and comfortable as possible, empowering our patients to live their best lives.</p>
  </div>

  <!-- Middle panel -->
  <div class="abs" style="left:395px;top:38px;width:330px">
    <div class="h-gold" style="font-size:19px">LEADERS IN MOBILE<br>ADVANCED WOUND CARE</div>
    <p style="font-size:10.2px;line-height:1.3;margin-top:4px">We provide a complete wound management program for our patients that includes the use of advanced treatments, the creation of care plans, and coordination of care with other clinicians. Our comprehensive in-home wound care services include</p>
    <div class="h-gold" style="font-size:15px;margin-top:8px">Advanced Wound Assessment</div>
    <p style="font-size:10.2px;line-height:1.3;margin-top:3px">Thorough evaluation of wound type, size, and stage to develop a tailored treatment plan.</p>
    <div class="h-gold" style="font-size:15px;margin-top:8px">Cutting-Edge Treatments</div>
    <p style="font-size:10.2px;line-height:1.3;margin:3px 0 6px">Utilization of the latest technologies &amp; techniques in wound care, including:</p>
    <ul class="treat-list">
      <li>Compression Biologic Skin Substitutes</li>
      <li>Surgical/ Trauma Wounds</li>
      <li>Negative Pressure Wound Therapy</li>
      <li>Venous/ Arterial Wounds</li>
      <li>Debridements</li>
      <li>Collagen &amp; Advanced Dressings</li>
    </ul>
  </div>
  <div class="photo photo--clinic" role="img" aria-label="Nurse placing an IV line for a seated patient" style="left:380px;top:392px;width:380px;height:488px;clip-path:polygon(0 12%,100% 0,100% 100%,0 100%)"></div>

  <!-- Right panel -->
  <div class="abs" style="left:785px;top:38px;width:330px">
    <div class="h-gold" style="font-size:19px">PERSONALIZED CARE PLANS</div>
    <p style="font-size:10.2px;line-height:1.3;margin-top:6px">Customized care plans designed to meet the specific needs of each patient, ensuring optimal healing. Coordination and direction of care for other caregivers and clinicians, including home health. Patient and Caregiver Education Providing education and support to patients and their caregivers to enhance understanding and promote self-care.</p>
  </div>
  <div class="photo photo--warm framed" role="img" aria-label="Nurse in a surgical cap checking a young man's ear" style="left:815px;top:188px;width:250px;height:210px"></div>

  <div class="abs h-gold" style="left:785px;top:472px;font-size:14.5px">Partner with Cedar Ridge Wounds:</div>
  <div class="partner" style="top:503px">
    <div class="partner__icon"><svg width="14" height="14" viewBox="0 0 14 14"><polyline points="2,7 6,11 12,3" fill="none" stroke="#fff" stroke-width="1.6"/></svg></div>
    <div><div class="partner__title">Enhanced Patient Outcomes</div><div class="partner__text">Our specialized expertise in advanced wound care leads to faster healing times &amp; improved patient satisfaction.</div></div>
  </div>
  <div class="partner" style="top:580px">
    <div class="partner__icon"><svg width="14" height="14" viewBox="0 0 14 14"><path d="M7 1a4 4 0 0 1 4 4c0 3-4 8-4 8S3 8 3 5a4 4 0 0 1 4-4z" fill="none" stroke="#fff" stroke-width="1.4"/></svg></div>
    <div><div class="partner__title">Extended Reach</div><div class="partner__text">Our in-home services allow your patients to receive high-quality care without the need for frequent visits, reducing the burden on your resources.</div></div>
  </div>
  <div class="partner" style="top:668px">
    <div class="partner__icon"><svg width="14" height="14" viewBox="0 0 14 14"><polyline points="2,7 6,11 12,3" fill="none" stroke="#fff" stroke-width="1.6"/></svg></div>
    <div><div class="partner__title">Professional Integrity</div><div class="partner__text">As a trusted partner, we uphold the highest standards of care and professionalism, reflecting positively on your clinic's reputation.</div></div>
  </div>
  <div class="partner" style="top:758px">
    <div class="partner__icon"><svg width="14" height="14" viewBox="0 0 14 14"><path d="M2 4h10M2 7h10M2 10h6" stroke="#fff" stroke-width="1.4"/></svg></div>
    <div><div class="partner__title">Seamless Collaboration</div><div class="partner__text">We maintain open communication with referring clinics, ensuring a coordinated approach to patient care.</div></div>
  </div>
</section>

</body>
</html>
```